■サイトマップ
1 TOP
2 Menu
3 Color
4 Improvement
5 Eyelash
6 About Us
7 Our Quality
8 Staff(一覧)
9 Staff(詳細)
10 Gallery(一覧)
11 Gallery(詳細)
12 Products(一覧)
13 Q & A
14 RECRUIT(一覧)
15 RECRUIT(詳細)
16 Topics(一覧)
17 Topics(詳細)
18 Contact

■希望デザインカラー
やさしい色味
ホワイト・ネイビー・ブラウン・ゴールド・グリーン・グレー
店舗や調度品の雰囲気に合うようにして、バランスはおまかせします。

■希望彩度・明度
ペール・ライト・パステル

■希望デザインテイスト
・好きなデザインイメージ
リラックス、フランク、カフェ、あたたかい、ナチュラル、優しい、清涼感、ボタニカル、高級感、ふんわり、シック、落ち着いた、丸みのある
└女性が通いたくなる、働きたくなるようなデザインで、写真多めの構成を希望
└スマホでの見え方や動きにも注力していただきたいです。(スライド・フリック・パララックス等)

・嫌いなデザインイメージ
可愛い・キュート・ポップ・ゴージャス・エレガント・幻想的・神秘的・重厚感・シック ・エッジ

■素材・ロゴ・サイトマップについて
・下記URLよりダウンロードしご使用ください。※現行サイトやポータルサイトから抽出いただいても構いません。
・素材は現行サイトより使用頂いてもOKですが、写真はなるべく添付のものをご使用ください。
・その他の写真素材はMorvique Stock( https://stock.morvique.com/jp/ )の通常アセットで購入できるカンプ画像を入れてください。
・Morvique Stockと定期契約をしており弊社負担となりますので、ランサー様に金額のご負担はございません。

URL:https://47.filebento.net/0319-3ad219e7b4f81c02a6d773e1b9c084e2
パスワード:4848
http://sorivel.co.jp/
青系、茶系、緑系、グレー系
【現行サイト】http://sorivel.co.jp/
【ポータルサイト】https://beauty.tamuloka.jp/slnK000482961/

■フォントについて
・無料フォントでの作成をお願いいたします。
・OSに紐づくフォントの使用はお控えください。 (ヒラギノなど)

■テキストについて
・なるべく、現行サイトやポータルサイト内の文章を配置して下さい。
「ここに文章が入ります。ここに文章が入ります。」等の同じ文言を繰り返すダミー文章は極力使用しないようお願いいたします。
ブログ・ニュースのタイトル部分などは「タイトルが入ります。」で大丈夫です。

■注意事項
・デザインの横幅は1300pxで作成をお願いいたします。
・申し訳ございませんがXD形式の納品はお受けできかねますのでご了承下さい。
・業務への支障となりますので、いかなるご用件であっても店舗へのご連絡は絶対にしないでください。
お世話になっております。
期間を延長し更に募ってまいります。
追加補足説明をさせていただきます。
使用する色味の関係上、どうしても「かっこいい感じ」になりがちですが、あくまで求めているのは女性らしいデザインとなりますので、角丸にしたり、色味にメリハリを付けたり、イラストをつける等で理想に近づけていただきたく存じます。
皆様お世話になっております。
最終期間まで延長し、更なバリエーションを募って参りたく存じます。
お付き合いの程何卒よろしくお願い申し上げます。
皆様お世話になっております。
選定に時間がかかっており申し訳ございません。
7月15日までには選定する予定ではございますので、何卒お待ちくださいますようお願い申し上げます、
皆様お世話になっております。
このたび7月31日まで、選定の期限を延長させていただきました。
もうしばらくのお付き合いのほど、何卒お願い申し上げます。

色味がよく、透明感のある雰囲気で作成くださいました。

皆様この度はご参加くださり誠にありがとうございました。
今後とも機会がございましたら何卒お付き合いのほどお願い申し上げます。

```html
<!DOCTYPE html>
<html lang="ja">
<head>
<meta charset="utf-8">
<title>LUVEA | Hair Salon</title>
<link rel="stylesheet" href="https://fonts.googleapis.com/css2?family=Marcellus&family=Noto+Sans+JP:wght@300;400;500&display=swap">
<style>
:root{
  --ink:#222;
  --muted:#8fa3ae;
  --accent:#a7b9c4;
  --mint:#a9dcd8;
  --mint-pale:#d7ecee;
  --pale:#f4f8fa;
  --footer:#7e99a7;
  --line:#dcdcdc;
  --black:#151515;
}
*{margin:0;padding:0;box-sizing:border-box}
html,body{width:1200px;height:4362px;overflow:hidden;background:#fff}
body{font-family:"Noto Sans JP",sans-serif;color:var(--ink)}
.page{position:relative;width:1200px;height:4362px;overflow:hidden}
.abs{position:absolute}
.serif{font-family:"Marcellus",serif}
.photo{position:absolute}
/* header */
.logo{position:absolute;font-family:"Marcellus",serif;font-size:40px;letter-spacing:2px;color:var(--ink)}
.nav a{position:absolute;top:41px;font-family:"Marcellus",serif;font-size:15px;color:var(--ink);text-decoration:none}
.btn{position:absolute;display:flex;align-items:center;justify-content:center;font-size:14px;border-radius:4px;text-decoration:none}
.btn-reserve{background:var(--mint);color:#fff}
.btn-contact{background:var(--black);color:#fff}
/* hero */
.hero-title{left:733px;top:200px;font-size:64px;line-height:70px;letter-spacing:2px}
.hero-sub{left:733px;top:430px;font-size:17px;letter-spacing:1px}
.intro{left:166px;top:700px;width:600px;text-align:center;font-size:16px;line-height:33px;letter-spacing:.5px}
/* section heads */
.sec-slash{position:absolute;width:36px;height:56px}
.sec-title{position:absolute;font-family:"Marcellus",serif;font-size:30px}
.sec-sub{position:absolute;font-size:13px;color:var(--muted);letter-spacing:1px}
.lead{position:absolute;font-size:21px;line-height:32px;letter-spacing:1px}
.body{position:absolute;font-size:14px;line-height:27px;letter-spacing:.3px}
.more{position:absolute;height:40px;border-bottom:1px solid var(--ink);font-size:14px;letter-spacing:.5px}
.more span{position:absolute;left:22px;top:14px}
.more i{position:absolute;right:-4px;top:2px;width:34px;height:34px;border-radius:50%;background:var(--accent)}
/* menu cards */
.card{position:absolute;top:1801px;width:287px;height:192px;display:flex;flex-direction:column;align-items:center;justify-content:center;color:#fff}
.card b{font-family:"Marcellus",serif;font-weight:400;font-size:23px}
.card small{font-size:13px;margin-top:10px}
/* topics */
.topic{position:absolute;left:225px;width:711px;height:48px;border-bottom:1px solid var(--line);font-size:14px}
.topic .d{position:absolute;left:9px;top:16px}
.topic .t{position:absolute;left:134px;top:16px}
/* footer */
.foot a{position:absolute;color:#fff;font-size:14px;text-decoration:none;font-family:"Marcellus",serif}
.social{position:absolute;top:4256px;width:24px;height:24px;border-radius:50%;background:var(--black)}
</style>
</head>
<body>
<div class="page">

<header>
  <div class="logo" style="left:74px;top:24px">LUVEA</div>
  <nav class="nav">
    <a style="left:352px">Top</a><a style="left:411px">Menu</a><a style="left:487px">About</a>
    <a style="left:563px">Gallery</a><a style="left:642px">Product</a><a style="left:726px">Topics</a><a style="left:800px">Recruit</a>
  </nav>
  <a class="btn btn-reserve" style="left:887px;top:29px;width:136px;height:45px">来店予約する</a>
  <a class="btn btn-contact" style="left:1026px;top:29px;width:139px;height:45px">CONTACT</a>
</header>

<section class="hero">
  <div class="photo" role="img" aria-label="Portrait of a woman with long dark hair against a pale background" style="left:83px;top:120px;width:774px;height:517px;background:linear-gradient(100deg,#eef0f1 0%,#d9c8be 35%,#e9e1da 55%,#f3f4f5 100%)"></div>
  <div class="abs" style="left:88px;top:620px;transform:rotate(-90deg);transform-origin:left top;font-size:12px;color:#333;white-space:nowrap">Morvique Stock | #472906318</div>
  <h1 class="abs serif hero-title" style="font-weight:400">SENCE<br>OF<br>BEAUTY</h1>
  <p class="abs hero-sub">美しさを追及するヘアサロン、LUVEA</p>
  <div class="photo" role="img" aria-label="Salon entrance wall with the shop sign and a potted plant" style="left:767px;top:516px;width:361px;height:374px;background:linear-gradient(180deg,#f6f6f4 0%,#eeeeec 70%,#a9b9d3 72%,#9fb1cd 100%)"></div>
  <p class="abs intro">LUVEAは、髪質改善・カラーに特化したヘアサロンです。<br>お客様一人ひとりのお悩みにしっかり応え、<br>最大限の魅力を引き出すためのご提案をさせていただきます。<br>こだわりのインテリアを並べた、明るく心地よい空間で、<br>リラックスしながらキレイを手に入れませんか？</p>
</section>

<svg width="0" height="0" style="position:absolute"><defs><symbol id="slash" viewBox="0 0 36 56"><line x1="34" y1="1" x2="2" y2="55" stroke="#bbb" stroke-width="1.2"/></symbol></defs></svg>

<section class="quality">
  <div class="photo" role="img" aria-label="Back view of long straight glossy brown hair in front of a gold mirror" style="left:0;top:1110px;width:274px;height:412px;background:linear-gradient(180deg,#d8d2b6 0%,#6b4f3e 40%,#4a372b 75%,#e8ebee 100%)"></div>
  <div class="photo" role="img" aria-label="Salon interior with styling chairs and mirrors" style="left:301px;top:1014px;width:273px;height:176px;background:linear-gradient(180deg,#e2dccd,#b9a88c 60%,#8a7763)"></div>
  <div class="photo" role="img" aria-label="Stylist chatting with a client at the mirror" style="left:301px;top:1221px;width:273px;height:181px;background:linear-gradient(90deg,#c9c3b8,#e6e2dc 50%,#b0a79a)"></div>
  <svg class="sec-slash" style="left:645px;top:1061px"><use href="#slash"/></svg>
  <h2 class="sec-title" style="left:681px;top:1076px;font-weight:400">Our Quality</h2>
  <p class="sec-sub" style="left:716px;top:1125px">サロンの特徴</p>
  <p class="lead" style="left:645px;top:1201px">月と太陽のような、<br>照らし照らされる大切な関係</p>
  <p class="body" style="left:645px;top:1328px;width:392px">少人数のプライベートサロンだからこそ、お客様一人ひとりに真摯に向き合います。<br>ご自宅でのケアやスタイリング方法も丁寧にお伝えし、再現しやすいヘアスタイルをご提供します。<br>当サロンとお客様は、月と太陽のような大切な関係。私たちLUVEAは、お客様の生活の一部として、欠かせない存在でありたいと思っております。</p>
  <a class="more" style="left:743px;top:1551px;width:163px"><span>VIEW MORE</span><i></i></a>
</section>

<section class="menu">
  <svg class="sec-slash" style="left:164px;top:1676px"><use href="#slash"/></svg>
  <h2 class="sec-title" style="left:200px;top:1695px;font-weight:400">Menu</h2>
  <p class="sec-sub" style="left:215px;top:1743px">メニュー</p>
  <div class="card" role="img" aria-label="Long sleek dark hair, hair improvement treatment" style="left:157px;background:linear-gradient(90deg,#6d7586,#4b4652 50%,#8c93a2)"><b>Improvement</b><small>髪質改善</small></div>
  <div class="card" role="img" aria-label="Woman with a copper bob, hair colour" style="left:457px;background:linear-gradient(90deg,#a1a0a0,#a86a45 50%,#8f8e90)"><b>Color</b><small>カラー</small></div>
  <div class="card" role="img" aria-label="Close-up of eyelash extension application" style="left:757px;background:linear-gradient(90deg,#ccbab2,#e6d4cc 50%,#d2c3bd)"><b>Eyelash</b><small>アイラッシュ</small></div>
  <a class="more" style="left:564px;top:2022px;width:161px"><span>VIEW MORE</span><i></i></a>
</section>

<section class="topics">
  <svg class="sec-slash" style="left:164px;top:2150px"><use href="#slash"/></svg>
  <h2 class="sec-title" style="left:196px;top:2166px;font-weight:400">Topics</h2>
  <p class="sec-sub" style="left:215px;top:2214px">お知らせ</p>
  <div class="topic" style="top:2257px"><span class="d">2023.07.01</span><span class="t">ホームページをリニューアルしました！</span></div>
  <div class="topic" style="top:2305px"><span class="d">2023.07.01</span><span class="t">ホームページをリニューアルしました！</span></div>
  <p class="abs" style="left:845px;top:2363px;font-size:14px">VIEW ALL</p>
  <p class="abs" style="left:930px;top:2363px;font-size:14px">&gt;</p>
</section>

<section class="gallery">
  <svg class="sec-slash" style="left:164px;top:2463px"><use href="#slash"/></svg>
  <h2 class="sec-title" style="left:200px;top:2477px;font-weight:400">Gallery</h2>
  <p class="sec-sub" style="left:222px;top:2525px">ギャラリー</p>
  <svg class="abs" style="left:176px;top:2702px" width="22" height="34"><polyline points="20,2 3,17 20,32" fill="none" stroke="#444" stroke-width="1.5"/></svg>
  <div class="photo" role="img" aria-label="Short black haircut style" style="left:229px;top:2600px;width:235px;height:253px;background:linear-gradient(180deg,#dfe3e6,#3a3633 40%,#4f6a4c 85%)"></div>
  <div class="photo" role="img" aria-label="Soft wavy medium-length style" style="left:483px;top:2600px;width:235px;height:253px;background:linear-gradient(180deg,#e7ecf1,#3c3636 45%,#e9e7e8 90%)"></div>
  <div class="photo" role="img" aria-label="Soft wavy medium-length style" style="left:735px;top:2600px;width:235px;height:253px;background:linear-gradient(180deg,#e7ecf1,#3c3636 45%,#e9e7e8 90%)"></div>
  <svg class="abs" style="left:1004px;top:2702px" width="22" height="34"><polyline points="2,2 19,17 2,32" fill="none" stroke="#444" stroke-width="1.5"/></svg>
</section>

<section class="recruit">
  <div class="abs" style="left:0;top:2946px;width:1200px;height:567px;background:var(--pale)"></div>
  <div class="abs serif" style="left:12px;top:3462px;transform:rotate(-90deg);transform-origin:left top;font-size:148px;line-height:120px;color:var(--mint-pale);white-space:nowrap">Recruit</div>
  <svg class="sec-slash" style="left:168px;top:3002px"><use href="#slash"/></svg>
  <h2 class="sec-title" style="left:203px;top:3016px;font-weight:400">Recruit</h2>
  <p class="sec-sub" style="left:215px;top:3065px">採用について</p>
  <p class="lead" style="left:203px;top:3140px">私たちと一緒に<br>LUVEAで働きませんか？</p>
  <p class="body" style="left:203px;top:3268px;width:332px">LUVEAでは、共に成長していける仲間を募集しております。ここにテキストが入りますここにテキストが入りますここにテキストが入りますここにテキストが入ります</p>
  <a class="more" style="left:303px;top:3396px;width:157px"><span>採用ページへ</span><i></i></a>
  <div class="photo" role="img" aria-label="Two stylists sitting in the salon" style="left:572px;top:3061px;width:473px;height:317px;background:linear-gradient(180deg,#e8e6e2,#5f6675 45%,#8a7b6b 75%,#cfc9c0)"></div>
</section>

<div class="photo" role="img" aria-label="Hair cutting scissors on a wooden table" style="left:0;top:3572px;width:1200px;height:318px;background:linear-gradient(100deg,#a88650,#d8b67a 40%,#c8a466 65%,#9c7a44)"></div>

<section class="access">
  <div class="photo" role="img" aria-label="Street map around the salon" style="left:0;top:3890px;width:462px;height:278px;background:linear-gradient(135deg,#e9e9e9,#dcdcdc)"></div>
  <div class="abs" style="left:462px;top:3890px;width:738px;height:278px;background:#f5f7f9"></div>
  <h2 class="abs serif" style="left:505px;top:3942px;font-size:38px;font-weight:400">Access</h2>
  <p class="abs" style="left:505px;top:4014px;font-size:13px">〒530-0099</p>
  <p class="abs" style="left:505px;top:4040px;font-size:13px;letter-spacing:1px">大阪府大阪市北区緑風町３丁目１２−４ 若葉ハイツ 2F</p>
  <p class="abs" style="left:505px;top:4076px;font-size:13px">Tel. <span style="font-size:22px;margin-left:6px">06-5000-4821</span></p>
  <a class="btn btn-contact" style="left:909px;top:3985px;width:186px;height:46px;border-radius:4px">CONTACT</a>
  <a class="btn btn-reserve" style="left:909px;top:4051px;width:186px;height:46px">来店予約する</a>
</section>

<footer class="foot">
  <div class="abs" style="left:0;top:4168px;width:1200px;height:194px;background:var(--footer)"></div>
  <div class="logo" style="left:51px;top:4262px;color:var(--black)">LUVEA</div>
  <a style="left:310px;top:4198px">Menu</a>
  <a style="left:315px;top:4228px">― Color</a>
  <a style="left:315px;top:4250px">― Improvement</a>
  <a style="left:315px;top:4272px">― Eyelash</a>
  <a style="left:518px;top:4196px">About</a>
  <a style="left:518px;top:4234px">Our Quality</a>
  <a style="left:518px;top:4272px">Product</a>
  <a style="left:692px;top:4194px">Topics</a>
  <a style="left:692px;top:4234px">Staff</a>
  <a style="left:692px;top:4270px">Gallery</a>
  <a style="left:835px;top:4194px">Recruit</a>
  <a style="left:835px;top:4232px">Q &amp; A</a>
  <a style="left:835px;top:4270px">Contact</a>
  <span class="social" style="left:987px"></span>
  <span class="social" style="left:1036px"></span>
  <span class="social" style="left:1087px"></span>
  <p class="abs" style="left:0;top:4332px;width:1200px;text-align:center;font-size:11px;color:var(--black)">©LUVEA.All Rights Reserved.</p>
</footer>

</div>
</body>
</html>
```